Comic, writer, and entrepreneur based in Los Angeles, CA

UPDATED BRIEF:

Need a PROFESSIONAL yet simultaneously sexy business card that will inspire those to go to my social media accounts and follow me.

Need all of my social media (logos on card, please) As well as my picture, which I will provide.

If there is a way where you could scan the business card from your phone and it would take you to the social media accounts that would be great too!

My goal is to get a comedy writing job at the Nightly Desk or WLR and also go on Pelican Pond once my app is fully functional and created.

But the business card is just something to give people when I am making connections in both the entrepreneurial world as well as the comedy world so it has to help me stand out in that way :).

#: 417-552-8904
Email: kbellin@mx.ovrk.edu
Pictogram: Rosalind_Q.K
Chirpr: @ThePalermoNotes
Craftlo: Rosa’s Clever Tops (website: https://www.craftlo-example.com/shop/RosasTp?ref=pr_shop_more)
VidStream: The Gagmistress (website: https://www.vidstream-example.com/channel/QRpLwVn4kZ-mTHbyqo8erxt7B )
Friendlink: /rosalind.bellin.71924
Website App: WarmFixerFolk.example (app in progress. Need emails to make a prototype.)

Target Market(s)

Talent agents needing TV writers and TV comedy personalities. Investors for my app.

Industry/Entity Type

Tv

Contact Information for Business Card

Can be double or single sided, whichever looks best. Green is my favorite color but I am open to anything. Maybe silver and green?! Just make it classy and sexy.

Colors

Designer to choose colors to be used in the design.

Requirements
Must have
• Chirpr: ThePalermoNotes
• Pictogram: Rosalind_q.k
• Vidstream: The Gagmistress
• Email: kbellin@mx.ovrk.edu
• Phone: 417-552-8904
• writer, comic, entrepreneur--or--comedy writer and entrepeneur
Nice to have
• Make me standout. I'm a star ;-). Please check out my social media for files or ideas. Thanks.

```html
<!DOCTYPE html>
<html lang="en">
<head>
<meta charset="utf-8">
<title>Rosalind Bellin — Business Card</title>
<link rel="stylesheet" href="https://fonts.googleapis.com/css2?family=Great+Vibes&family=Tinos&display=swap">
<style>
  :root {
    --pink: #e0439c;
    --ink: #111111;
    --paper: #ffffff;
    --stage: #3a3a3c;
    --photo-warm: #d9b48f;
    --photo-cool: #8a8f99;
  }
  * { margin: 0; padding: 0; box-sizing: border-box; }
  html, body {
    width: 1200px; height: 880px; overflow: hidden;
    background: var(--stage);
  }
  .canvas { position: relative; width: 1200px; height: 880px; }
  .card {
    position: absolute; width: 700px; height: 400px;
    border-radius: 28px; overflow: hidden;
    box-shadow: 0 10px 28px rgba(0,0,0,.45);
  }
  .card-back { left: 150px; top: 27px; background: var(--pink); }
  .card-front { left: 350px; top: 453px; background: var(--paper); }
  .card svg.art { position: absolute; inset: 0; }

  .back-content {
    position: absolute; inset: 0;
    display: flex; flex-direction: column;
    align-items: center; justify-content: center;
    color: var(--paper); font-family: "Tinos", serif;
  }
  .brand-name {
    display: flex; align-items: center; gap: 14px;
    font-size: 40px; line-height: 1;
  }
  .brand-dot {
    width: 18px; height: 18px; border-radius: 50%;
    background: var(--paper);
  }
  .social-list {
    list-style: none; margin-top: 30px;
    font-size: 19px; line-height: 1.5; text-align: center;
  }

  .details { position: absolute; left: 346px; top: 110px; }
  .details .name {
    font-family: "Great Vibes", cursive; font-size: 50px;
    color: var(--pink); line-height: 1; word-spacing: 10px;
  }
  .details .roles {
    font-family: "Tinos", serif; font-size: 19px;
    color: var(--ink); margin: 6px 0 0 34px;
  }
  .details .contact {
    font-family: "Tinos", serif; font-size: 19px;
    color: var(--ink); margin: 32px 0 0 34px; line-height: 1.4;
  }
</style>
</head>
<body>
<main class="canvas">

  <section class="card card-back" aria-label="Card back">
    <div class="back-content">
      <div class="brand-name"><span class="brand-dot"></span>Rosalind Bellin</div>
      <ul class="social-list">
        <li>Chirpr: @ThePalermoNotes</li>
        <li>Pictogram: Rosalind_q.k</li>
        <li>VidStream: The Gagmistress</li>
      </ul>
    </div>
  </section>

  <section class="card card-front" aria-label="Card front">
    <svg class="art" width="700" height="400" viewBox="0 0 700 400">
      <defs>
        <radialGradient id="portrait-tone" cx="50%" cy="40%" r="60%">
          <stop offset="0%" stop-color="var(--photo-warm)"/>
          <stop offset="100%" stop-color="var(--photo-cool)"/>
        </radialGradient>
        <clipPath id="portrait-clip"><circle cx="178" cy="238" r="94"/></clipPath>
      </defs>
      <rect class="band-pink" width="700" height="400" fill="var(--pink)"/>
      <path class="swoosh-black" fill="var(--ink)"
            d="M0,96 C240,52 470,90 590,0 L700,0 L700,300 C520,316 300,346 0,388 Z"/>
      <path class="panel-white" fill="var(--paper)"
            d="M0,108 C250,66 490,104 640,0 L700,0 L700,272 C520,290 290,322 0,376 Z"/>
      <circle class="photo-ring-black" cx="162" cy="236" r="118" fill="var(--ink)"/>
      <circle class="photo-ring-pink" cx="178" cy="238" r="98" fill="var(--pink)"/>
      <rect role="img" aria-label="Portrait photo of Rosalind Bellin"
            x="84" y="144" width="188" height="188"
            fill="url(#portrait-tone)" clip-path="url(#portrait-clip)"/>
    </svg>
    <div class="details">
      <div class="name">Rosalind Bellin</div>
      <div class="roles">writer, comic, entrepreneur</div>
      <div class="contact">
        <div>Email: kbellin@mx.ovrk.edu</div>
        <div>Phone: 417-552-8904</div>
      </div>
    </div>
  </section>

</main>
</body>
</html>
```